Stationery Design needed for logo design project

We are looking for a new stationary design for all templates, business cards, letterheads, envelopes, pads, stamps and accessories. It needs to be unique, slick, and ooze premium quality. The details to go on the stationary are as follows:
Name: The Fernmoor Dental Clnic, Dentist: Dr. Kevin Dunleavy BDS NUI (hons), Dr. Philippa Cranley BScDent BA (separate card per dentist) tel: 0407 58291 add: The Fernmoor Dental Clinic, Riverside Medical Hub, Knockrobin, Wicklow Town, County Wicklow. web: www.thefernmoordentalclinic.ie email: info@thefernmoordentalclinic.ie
Colour pallet is: primary blue, white, secondary black and grey.
We have attached all source files for the logo below. We want a textured card, with embossed, icons and name on front, no need to repeat it o the reverse. True blue would be the dominant colour.
Besides this let your imagination go wild.
Thank you. TFDC.

```html
<!DOCTYPE html>
<html lang="en">
<head>
<meta charset="utf-8">
<title>The Fernmoor Dental Clinic — Stationery</title>
<link href="https://fonts.googleapis.com/css2?family=Questrial&family=Arimo:wght@400;700&display=swap" rel="stylesheet">
<style>
  :root {
    --blue: #2f8ac8;
    --grey: #58595b;
    --ink: #333638;
    --muted: #6d6f72;
    --paper: #ffffff;
    --backdrop: #eceded;
    --line: #d9dadb;
  }
  * { box-sizing: border-box; margin: 0; padding: 0; }
  html, body { width: 1200px; height: 937px; overflow: hidden; }
  body { background: var(--backdrop); font-family: "Arimo", Arial, sans-serif; color: var(--ink); position: relative; }

  .sheet { position: absolute; background: var(--paper); overflow: hidden; }
  .brand { display: flex; align-items: center; font-family: "Questrial", sans-serif; color: var(--grey); white-space: nowrap; }
  .brand-square { background: var(--blue); border-radius: 3px; flex: none; }
  .footer { position: absolute; left: 0; bottom: 0; display: block; }
  .footer-url { position: absolute; font-family: "Questrial", sans-serif; color: #fff; white-space: nowrap; letter-spacing: .04em; }

  /* Letterhead */
  .letterhead { left: 184px; top: 66px; width: 389px; height: 546px; }
  .letterhead .brand { position: absolute; left: 18px; top: 30px; font-size: 10.5px; }
  .letterhead .brand-square { width: 15px; height: 15px; margin-right: 6px; }
  .contact-block { position: absolute; right: 16px; top: 23px; text-align: right; font-size: 5.2px; line-height: 7.4px; color: var(--ink); }
  .contact-block .web { color: var(--blue); }
  .letter-body { position: absolute; left: 36px; top: 140px; width: 300px; font-size: 5.3px; line-height: 7.6px; color: var(--ink); }
  .letter-body p { margin-bottom: 9px; }
  .letter-body .gap { margin-bottom: 22px; }
  .letter-body strong { font-weight: 700; }
  .signature-mark { width: 40px; height: 18px; background: #e7e7e7; margin: -2px 0 6px; }

  /* Blank sheet */
  .cover { left: 636px; top: 40px; width: 460px; height: 576px; }
  .cover .brand { position: absolute; left: 0; right: 0; top: 300px; justify-content: center; font-size: 22px; letter-spacing: .02em; }
  .cover .brand-square { width: 38px; height: 38px; margin-right: 14px; border-radius: 5px; }

  /* Business cards */
  .card { width: 177px; height: 100px; left: 45px; }
  .card-front { top: 658px; }
  .card-back { top: 785px; height: 99px; }
  .card-front .brand { position: absolute; right: 12px; top: 13px; font-size: 7.5px; }
  .card-front .brand-square { width: 11px; height: 11px; margin-right: 4px; border-radius: 2px; }
  .holder-name { position: absolute; left: 10px; top: 34px; font-size: 8.5px; color: var(--blue); font-weight: 700; }
  .holder-role { position: absolute; left: 10px; top: 46px; font-size: 5.5px; color: var(--ink); }
  .card-rule { position: absolute; left: 10px; right: 12px; top: 44px; height: 1px; background: var(--blue); opacity: .5; }
  .card-contact { position: absolute; right: 12px; top: 54px; text-align: right; font-size: 4.4px; line-height: 6px; color: var(--ink); }
  .card-back .brand { position: absolute; left: 0; right: 0; top: 40px; justify-content: center; font-size: 9px; }
  .card-back .brand-square { width: 13px; height: 13px; margin-right: 5px; border-radius: 2px; }

  /* Envelope front */
  .envelope-front { left: 264px; top: 672px; width: 433px; height: 208px; }
  .envelope-front .brand { position: absolute; left: 14px; top: 24px; font-size: 10.5px; }
  .envelope-front .brand-square { width: 16px; height: 16px; margin-right: 6px; }
  .envelope-address { position: absolute; left: 14px; top: 48px; font-family: "Questrial", sans-serif; font-size: 6.6px; color: var(--muted); }

  /* Envelope back */
  .envelope-back { left: 736px; top: 672px; width: 433px; height: 208px; }
  .envelope-flap { position: absolute; left: 0; top: 0; width: 100%; height: 72px; background: var(--grey); border-radius: 0 0 52px 52px / 0 0 44px 44px; display: flex; align-items: center; justify-content: center; }
  .envelope-flap span { font-family: "Questrial", sans-serif; color: #fff; font-size: 13px; letter-spacing: .14em; }
</style>
</head>
<body>

  <!-- Letterhead -->
  <section class="sheet letterhead">
    <div class="brand"><span class="brand-square"></span>The Fernmoor Dental Clinic</div>
    <div class="contact-block">
      <div>Riverside Medical Hub</div>
      <div>Knockrobin WT</div>
      <div>0407 58291</div>
      <div>info@thefernmoordentalclinic.ie</div>
      <div class="web">www.thefernmoordentalclinic.ie</div>
    </div>
    <div class="letter-body">
      <p>July 2, 2012</p>
      <p><strong>Dear Cili,</strong><br>ABC Building, def St., Country Name</p>
      <p>Thank you for choosing our clinic for your dental care. This letter confirms the details of your next visit and explains what to expect on the day. Please arrive ten minutes early so our reception team can update your records and answer any questions. If you need to change the time, call us at least one day ahead and we will gladly find a new slot that suits you and your family.</p>
      <p class="gap">Our team looks forward to welcoming you and keeping your smile healthy and bright for many years to come.</p>
      <p>Along with routine checkups we offer cleaning, whitening, fillings and gentle care for nervous patients. Our modern rooms and calm staff make each visit relaxed and simple. Parking is free on site and the clinic is fully accessible. We also welcome new patients of every age, so please share our details with friends and neighbours who may be looking for a trusted local dentist.</p>
      <p>Best Regards,</p>
      <div class="signature-mark" role="img" aria-label="Handwritten signature"></div>
      <p><strong>Martin Keogh</strong><br>Director<br><br>ABC Building, def St., Country Name</p>
    </div>
    <svg class="footer" width="389" height="20" viewBox="0 0 389 20">
      <path d="M0 0 H138 Q150 0 156 20 H0 Z" fill="var(--grey)"/>
      <rect x="158" y="12" width="231" height="8" fill="var(--blue)"/>
    </svg>
    <span class="footer-url" style="left:12px; bottom:5px; font-size:7px;">www.thefernmoordentalclinic.ie</span>
  </section>

  <!-- Cover sheet -->
  <section class="sheet cover">
    <div class="brand"><span class="brand-square"></span>The Fernmoor Dental Clinic</div>
    <svg class="footer" width="460" height="17" viewBox="0 0 460 17">
      <path d="M0 0 H166 Q180 0 186 17 H0 Z" fill="var(--grey)"/>
      <rect x="188" y="10" width="272" height="7" fill="var(--blue)"/>
    </svg>
    <span class="footer-url" style="left:12px; bottom:4px; font-size:7.5px;">www.thefernmoordentalclinic.ie</span>
  </section>

  <!-- Business card front -->
  <section class="sheet card card-front">
    <div class="brand"><span class="brand-square"></span>The Fernmoor Dental Clinic</div>
    <div class="holder-name">Ciaran M Doyle</div>
    <div class="card-rule"></div>
    <div class="holder-role">CEO</div>
    <div class="card-contact">
      <div>Riverside Medical Hub</div>
      <div>Knockrobin WT</div>
      <div>0407 58291</div>
      <div>info@thefernmoordentalclinic.ie</div>
      <div>www.thefernmoordentalclinic.ie</div>
    </div>
    <svg class="footer" width="177" height="10" viewBox="0 0 177 10">
      <path d="M0 0 H62 Q68 0 71 10 H0 Z" fill="var(--grey)"/>
      <rect x="72" y="6" width="105" height="4" fill="var(--blue)"/>
    </svg>
    <span class="footer-url" style="left:4px; bottom:2px; font-size:3.6px;">www.thefernmoordentalclinic.ie</span>
  </section>

  <!-- Business card back -->
  <section class="sheet card card-back">
    <div class="brand"><span class="brand-square"></span>The Fernmoor Dental Clinic</div>
    <svg class="footer" width="177" height="10" viewBox="0 0 177 10">
      <rect x="0" y="6" width="105" height="4" fill="var(--blue)"/>
      <path d="M177 0 H115 Q109 0 106 10 H177 Z" fill="var(--grey)"/>
    </svg>
    <span class="footer-url" style="right:4px; bottom:2px; font-size:3.6px;">www.thefernmoordentalclinic.ie</span>
  </section>

  <!-- Envelope front -->
  <section class="sheet envelope-front">
    <div class="brand"><span class="brand-square"></span>The Fernmoor Dental Clinic</div>
    <div class="envelope-address">Riverside Medical Hub, Knockrobin WT</div>
    <svg class="footer" width="433" height="19" viewBox="0 0 433 19">
      <path d="M0 0 H160 Q172 0 177 19 H0 Z" fill="var(--grey)"/>
      <rect x="179" y="12" width="254" height="7" fill="var(--blue)"/>
    </svg>
    <span class="footer-url" style="left:10px; bottom:5px; font-size:8px;">www.thefernmoordentalclinic.ie</span>
  </section>

  <!-- Envelope back -->
  <section class="sheet envelope-back">
    <div class="envelope-flap"><span>www.thefernmoordentalclinic.ie</span></div>
  </section>

</body>
</html>
```